Vision, Mission and Culture Posters

We have written text paragraphs for our company vision and mission and need them made into a2 or a3 sized posters using our logo for inspiration for colour. Our company culture has 10 paragraphs and we'd like this to be a single poster of a2 or a1. Each poster should have the logo on and share common design. It's not a complex job really.

Industry/Entity Type

It Company

Requirements
Nice to have
• These will be going up on our office wall so need to be clear to read from a distance and look professional but also not stodgy.

```html
<!DOCTYPE html>
<html lang="en">
<head>
<meta charset="utf-8">
<title>Bayline Parking – Mission Poster</title>
<link rel="stylesheet" href="https://fonts.googleapis.com/css2?family=Open+Sans:wdth,wght@75..100,300..800&display=swap">
<style>
  :root {
    --paper-centre: #fffef4;
    --paper-edge: #fbf3b8;
    --brand-red: #ec2227;
    --ink: #000000;
    --navy: #243571;
    --sky: #a9dbef;
    --name-ink: #1a1a1a;
  }
  html, body {
    margin: 0;
    padding: 0;
    width: 848px;
    height: 1200px;
    overflow: hidden;
  }
  .poster {
    position: relative;
    width: 848px;
    height: 1200px;
    overflow: hidden;
    background: radial-gradient(ellipse at 50% 55%, var(--paper-centre) 0%, var(--paper-centre) 35%, var(--paper-edge) 100%);
    font-family: "Open Sans", Arial, sans-serif;
  }
  .brand {
    position: absolute;
    top: 78px;
    left: 0;
    width: 848px;
    display: flex;
    justify-content: center;
    align-items: center;
    gap: 18px;
  }
  .brand-mark {
    width: 40px;
    height: 40px;
    background: var(--brand-red);
  }
  .brand-name {
    font-size: 48px;
    font-weight: 700;
    color: var(--name-ink);
    line-height: 1;
    letter-spacing: 0.5px;
  }
  .mission {
    margin: 0;
    font-weight: inherit;
  }
  .line {
    position: absolute;
    white-space: nowrap;
    line-height: 1;
  }
  .light { font-weight: 300; color: var(--ink); }
  .regular { font-weight: 400; color: var(--ink); }
  .strong { font-weight: 700; color: var(--ink); }
  .accent { font-weight: 700; color: var(--brand-red); }
  .condensed { font-stretch: 75%; font-weight: 700; }

  .l-to         { left: 313px; top: 240px; font-size: 70px; }
  .l-provide    { left: 208px; top: 296px; font-size: 79px; letter-spacing: -1px; }
  .l-most       { left: 298px; top: 362px; font-size: 78px; }
  .l-hassle     { left: 40px;  top: 424px; font-size: 108px; letter-spacing: -2px; }
  .l-rental     { left: 270px; top: 527px; font-size: 77px; letter-spacing: -1px; }
  .l-whilst     { left: 80px;  top: 596px; font-size: 81px; letter-spacing: -1px; }
  .l-personal   { left: 158px; top: 656px; font-size: 90px; letter-spacing: -1px; }
  .l-personal .light { font-size: 74px; }
  .l-customer   { left: 333px; top: 719px; font-size: 88px; letter-spacing: -1px; }
  .l-experience { left: 118px; top: 792px; font-size: 80px; letter-spacing: -1px; }
  .l-want       { left: 275px; top: 862px; font-size: 79px; letter-spacing: -1px; }
  .l-friends    { left: 232px; top: 933px; font-size: 80px; letter-spacing: -1px; }
  .l-about      { left: 483px; top: 1015px; font-size: 78px; }

  .footer-art {
    position: absolute;
    left: 0;
    bottom: 0;
    width: 848px;
    height: 120px;
    background: radial-gradient(ellipse 70% 100% at 18% 100%, var(--navy) 0%, var(--navy) 45%, var(--sky) 70%, rgba(169, 219, 239, 0) 100%);
  }
</style>
</head>
<body>
<div class="poster">
  <header class="brand">
    <span class="brand-mark"></span>
    <span class="brand-name">Bayline Parking</span>
  </header>

  <h1 class="mission">
    <span class="line light l-to">To</span>
    <span class="line accent l-provide">provide</span>
    <span class="line light l-most">the&nbsp; most</span>
    <span class="line accent condensed l-hassle">hassle-free parking</span>
    <span class="line strong l-rental">rental service</span>
    <span class="line light l-whilst">whilst giving</span>
    <span class="line l-personal"><span class="light">a </span><span class="accent">personal</span></span>
    <span class="line accent l-customer">customer</span>
    <span class="line light l-experience">experience people</span>
    <span class="line light l-want">want to tell</span>
    <span class="line accent l-friends">their friends</span>
    <span class="line regular l-about">about</span>
  </h1>

  <div class="footer-art" role="img" aria-label="Decorative navy and sky-blue wave band along the bottom edge"></div>
</div>
</body>
</html>
```